Poster - Series of Poster Designs

We have a number of motivational quotes related to weight loss and fitness which need putting into a series of posters.
The designs need to:
- Reflect the current brand (see www.hillwardhavens.com.au)
- Be designed with scalability in mind to fit to A1, A3, A4, and A5. All portrait layout.
- Incorporate our logo
- Any images need to relfect the diversity of our clients ranging from 70kgs up to 200kgs.
- We have a stock of photos which can be used, or you can source your own (subject to budget approval)
Total of 26 posters in total, but all on the same design series (so effectively 1 design, with 26 applications).
The series of quotes are attached. An example quote would be:
-
"The difference between your body this week and next week is what you do for the next seven days to achieve your goals"
-
Our clients are a range of ages (20 - 60) and split male/female so colours should be neutral and reflect our orange/green branding. A modern feel but not super modern.
Output needs to be A3 ready to print with all source files included so that we can amend in the future.
There may be ongoing work for the right designer.

```html
<!DOCTYPE html>
<html lang="en">
<head>
<meta charset="utf-8">
<title>Hillward Havens – Motivation Poster</title>
<link rel="stylesheet" href="https://fonts.googleapis.com/css2?family=Alfa+Slab+One&family=Arvo&family=Kaushan+Script&family=Raleway:wght@300;500&display=swap">
<style>
  :root {
    --ink: #4a1e12;
    --panel: rgba(255, 250, 240, 0.38);
    --panel-edge: rgba(255, 255, 255, 0.55);
    --forest-deep: #2f3a1c;
    --forest-mid: #6a6a2a;
    --leaf-warm: #a4552a;
    --sun: #fff3c2;
    --white: #ffffff;
  }
  html, body {
    margin: 0;
    padding: 0;
    width: 848px;
    height: 1200px;
    overflow: hidden;
    background: var(--white);
  }
  .poster {
    position: relative;
    width: 848px;
    height: 1200px;
    overflow: hidden;
  }
  .poster__photo {
    position: absolute;
    inset: 0;
    background:
      radial-gradient(circle at 82% 8%, var(--sun) 0%, rgba(255, 230, 150, 0.7) 14%, rgba(255, 210, 120, 0) 42%),
      radial-gradient(ellipse at 50% 55%, rgba(210, 200, 120, 0.75) 0%, rgba(160, 150, 80, 0) 45%),
      linear-gradient(180deg, var(--forest-mid) 0%, var(--forest-deep) 35%, #5a4a22 65%, var(--leaf-warm) 85%, #6b4a34 100%);
  }
  .quote-panel {
    position: absolute;
    left: 190px;
    top: 145px;
    width: 462px;
    height: 873px;
    background: var(--panel);
    border: 1px solid var(--panel-edge);
    box-sizing: border-box;
  }
  .quote {
    position: absolute;
    inset: 0;
    color: var(--ink);
    text-align: center;
  }
  .quote__line {
    position: absolute;
    left: 0;
    width: 848px;
    margin: 0;
    line-height: 1;
    white-space: nowrap;
  }
  .quote__script {
    font-family: "Kaushan Script", cursive;
    font-weight: 400;
  }
  .quote__spaced {
    font-family: "Raleway", sans-serif;
    font-weight: 300;
    font-size: 32px;
    letter-spacing: 34px;
    text-indent: 34px;
  }
  .quote__heavy {
    font-family: "Alfa Slab One", serif;
    font-size: 76px;
  }
  .quote__slab {
    font-family: "Arvo", serif;
  }
  .quote__caps {
    font-family: "Raleway", sans-serif;
    font-weight: 500;
    font-size: 26px;
    letter-spacing: 1.5px;
    text-transform: uppercase;
  }
  .brand-tile {
    position: absolute;
    left: 314px;
    top: 1010px;
    width: 214px;
    height: 108px;
    background: var(--white);
    display: flex;
    align-items: center;
    justify-content: center;
  }
  .brand-tile__name {
    font-family: "Raleway", sans-serif;
    font-weight: 500;
    font-size: 18px;
    color: var(--ink);
  }
</style>
</head>
<body>
  <main class="poster">
    <div class="poster__photo" role="img" aria-label="Sunlit forest trail with stone steps winding through twisted trees and fallen autumn leaves"></div>

    <div class="quote-panel"></div>

    <section class="quote" aria-label="Motivational quote">
      <p class="quote__line quote__script" style="top:204px;font-size:42px;">The</p>
      <p class="quote__line quote__script" style="top:244px;font-size:46px;">difference</p>
      <p class="quote__line quote__spaced" style="top:318px;">between</p>
      <p class="quote__line quote__heavy" style="top:366px;">your body</p>
      <p class="quote__line quote__heavy" style="top:437px;">this week</p>
      <p class="quote__line quote__slab" style="top:524px;font-size:38px;">and</p>
      <p class="quote__line quote__slab" style="top:578px;font-size:70px;">next week</p>
      <p class="quote__line quote__caps" style="top:677px;">is what you do</p>
      <p class="quote__line quote__caps" style="top:706px;">for the next</p>
      <p class="quote__line quote__slab" style="top:744px;font-size:72px;">7 days</p>
      <p class="quote__line quote__caps" style="top:843px;">to achieve</p>
      <p class="quote__line quote__script" style="top:884px;font-size:64px;">your goals</p>
    </section>

    <div class="brand-tile" aria-label="Hillward Havens Retreat">
      <span class="brand-tile__name">Hillward Havens</span>
    </div>
  </main>
</body>
</html>
```